Power Point for a new training package

I am a new business and about to offer my first teaching day. I have all the content, have a logo etc. but need to translate this into a slick bespoke Power Point presentation,

Target Market(s)

Senior people in healthcare sector, UK

Industry/Entity Type

Healthcare

Requirements
Must have
• Sense of originality, use of my logo and associated colour scheme, stylish but simple

```html
<!DOCTYPE html>
<html lang="en">
<head>
<meta charset="utf-8">
<title>Verran Hale Consulting – Presentation Deck</title>
<link href="https://fonts.googleapis.com/css2?family=Montserrat:ital,wght@0,400;0,500;0,600;0,700;0,800;1,500&display=swap" rel="stylesheet">
<style>
:root{
  --teal:#27bdb3;
  --teal-light:#4fd6cb;
  --teal-deep:#16a59b;
  --ink:#1f1f1f;
  --grey:#6b6b6b;
  --soft:#f1f1f1;
  --page:#e4e5e7;
  --white:#ffffff;
}
*{box-sizing:border-box;margin:0;padding:0}
html,body{width:906px;height:1200px;overflow:hidden;background:var(--page);font-family:'Montserrat',sans-serif;color:var(--ink)}
.deck{position:relative;width:906px;height:1200px}
.slide{position:absolute;width:267px;height:151px;background:var(--white);box-shadow:0 1px 3px rgba(0,0,0,.22);overflow:hidden}
.slide > *{position:absolute}
.slide-title{left:10px;top:7px;font-size:9px;font-weight:700;letter-spacing:.1px}
.title-rule{left:10px;top:20px;width:30px;height:1.5px;background:var(--teal)}
.title-rule::before{content:"";position:absolute;left:0;top:2.5px;width:5px;height:1px;border-top:1px dotted var(--teal)}
.brand{right:8px;top:7px;display:flex;align-items:center;gap:2px;font-size:3px;font-weight:600;line-height:1}
.brand-dot{width:6px;height:6px;border:.8px solid var(--teal);border-radius:50%}
.footer{left:6px;bottom:5px;display:flex;align-items:center;gap:2px;font-size:1.8px;font-weight:600}
.footer .brand-dot{width:5px;height:5px}
.footer-rule{left:30px;right:14px;bottom:7px;height:.4px;background:var(--teal)}
.page-no{right:7px;bottom:5px;font-size:2.6px;font-weight:600}
.tiny{font-size:2.4px;line-height:1.4;color:var(--grey)}
.small{font-size:3.4px;line-height:1.4;color:var(--grey)}
.head{font-size:4px;font-weight:700;color:var(--ink)}
.teal{color:var(--teal)}
.placeholder{background:linear-gradient(135deg,#c9d4d8,#8aa1a8)}
.icon-circle{border-radius:50%;background:var(--teal);display:flex;align-items:center;justify-content:center}
</style>
</head>
<body>
<main class="deck">

<!-- 1 cover -->
<section class="slide cover" style="left:38px;top:36px;background:linear-gradient(120deg,#3cc8be,#2cbcb2)">
  <div style="left:28px;top:40px;width:62px;height:62px;border:3px solid rgba(255,255,255,.45);border-radius:50%"></div>
  <div style="left:110px;top:58px;color:#1f1f1f;font-size:12px;font-weight:600;line-height:1.05">Verran Hale<br><span style="font-weight:400">Consulting</span></div>
  <div style="left:104px;top:89px;width:163px;height:10px;background:#fff;padding-left:6px;font-size:6px;font-weight:500;letter-spacing:.6px;color:var(--teal);line-height:10px">Presentation Business Marketing</div>
  <div style="left:112px;top:104px;font-size:3px;letter-spacing:1px;color:#1f1f1f">verranhaleconsulting.com</div>
</section>

<!-- 2 title -->
<section class="slide" style="left:320px;top:36px;background:linear-gradient(90deg,#fff,#f0f0f0)">
  <div style="left:28px;top:13px;width:14px;height:14px;border:1px solid var(--teal);border-radius:50%"></div>
  <div style="left:17px;top:30px;font-size:6px;font-weight:500;line-height:1.1;text-align:center">Verran Hale<br><span style="font-weight:400">Consulting</span></div>
  <div style="left:16px;top:66px;font-size:15px;font-weight:800">Business</div>
  <div style="left:16px;top:82px;font-size:10px;font-weight:700;color:var(--teal)">Marketing</div>
  <div style="left:16px;top:107px;font-size:6px;font-style:italic;font-weight:500">Presentation</div>
  <div class="tiny" style="left:16px;top:116px;width:80px">Lorem ipsum dolor sit amet, consectetuer adipiscing elit, sed diam nonum</div>
  <div style="left:16px;top:135px;display:flex;gap:2px"><i style="width:3px;height:3px;border-radius:50%;background:#1f1f1f"></i><i style="width:3px;height:3px;border-radius:50%;background:var(--teal)"></i><i style="width:3px;height:3px;border-radius:50%;background:#1f1f1f"></i></div>
  <div class="placeholder" role="img" aria-label="Portrait photograph of the consultant in a suit" style="left:112px;top:0;width:155px;height:122px;background:linear-gradient(90deg,#9a9a9a,#3c4a5e 60%,#aaa)"></div>
  <div style="left:112px;top:122px;width:155px;height:29px;background:var(--teal);color:#fff;font-size:4px;letter-spacing:1.4px;text-align:center;line-height:29px">verranhaleconsulting.com</div>
</section>

<!-- 3 agenda -->
<section class="slide" style="left:601px;top:36px">
  <div class="brand"><span class="brand-dot"></span>Verran Hale<br>Consulting</div>
  <div style="left:43px;top:68px;width:25px;height:1.5px;background:var(--teal)"></div>
  <div style="left:43px;top:70px;font-size:15px;font-weight:700">Agenda</div>
  <div style="left:43px;top:89px;width:25px;height:1.5px;background:var(--teal)"></div>
  <div style="left:134px;top:37px;width:110px">
    <div class="head"><span class="teal">1.</span> Lorem ipsum</div><div class="tiny" style="padding-left:6px;margin-bottom:8px">Lorem ipsum dolor sit amet, consectetuer adipiscing elit, sed diam nonummy nibh euismod tincid</div>
    <div class="head"><span class="teal">2.</span> Lorem ipsum</div><div class="tiny" style="padding-left:6px;margin-bottom:8px">Lorem ipsum dolor sit amet, consectetuer adipiscing elit, sed diam nonummy nibh euismod tincid</div>
    <div class="head"><span class="teal">3.</span> Lorem ipsum</div><div class="tiny" style="padding-left:6px;margin-bottom:8px">Lorem ipsum dolor sit amet, consectetuer adipiscing elit, sed diam nonummy nibh euismod tincid</div>
    <div class="head"><span class="teal">4.</span> Lorem ipsum</div><div class="tiny" style="padding-left:6px">Lorem ipsum dolor sit amet, consectetuer adipiscing elit, sed diam nonummy nibh euismod tincid</div>
  </div>
  <div class="footer"><span class="brand-dot"></span>©2023. Verran Hale Consulting Ltd</div>
  <div class="page-no">2</div>
</section>

<!-- 4 intro -->
<section class="slide" style="left:38px;top:200px">
  <div class="brand"><span class="brand-dot"></span>Verran Hale<br>Consulting</div>
  <div style="left:12px;top:11px;font-size:8px;font-weight:700;line-height:1.3">Lorem Ipsum<br>Dolor Sit<br>Ametkeeper.</div>
  <div class="title-rule" style="top:47px;left:12px;width:6px"></div>
  <div class="tiny" style="left:12px;top:53px;width:68px;text-align:justify">Lorem ipsum dolor sit amet, consectetuer adipiscing elit, sed diam nonummy nibh euismod tincidunt ut laoreet dolore magna aliquam erat volutpat.<br><br>Ut wisi enim ad minim veniam, quis nostrud exerci tation ullamcorper suscipit lobortis nisl ut aliquip ex ea commodo consequat. Duis autem vel eum iriure dolor in hendrerit in vulputate velit esse molestie consequat.<br><br>vel illum dolore eu feugiat nulla facilisis at vero eros et accumsan et iusto odio dignissim qui blandit praesent</div>
  <div class="placeholder" role="img" aria-label="Photograph of clinicians working in a hospital ward" style="left:93px;top:25px;width:174px;height:50px;background:linear-gradient(90deg,#b8c8d2,#6f8797,#c6d3db)"></div>
  <div style="left:116px;top:64px;width:47px;height:66px;background:#fff;box-shadow:0 .5px 2px rgba(0,0,0,.2)"></div>
  <div style="left:181px;top:64px;width:47px;height:66px;background:#fff;box-shadow:0 .5px 2px rgba(0,0,0,.2)"></div>
  <div style="left:116px;top:64px;width:47px;height:12px;background:var(--teal);color:#fff;font-size:7px;font-weight:600;text-align:center;line-height:12px">Text Here</div>
  <div style="left:181px;top:64px;width:47px;height:12px;background:var(--teal);color:#fff;font-size:7px;font-weight:600;text-align:center;line-height:12px">Text Here</div>
  <div class="tiny" style="left:119px;top:79px;width:41px">Lorem ipsum dolor sit amet, consectetuer adipiscing elit, sed diam nonummy nibh euismod tincidunt ut laoreet dolore magna aliquam erat volutpat.<br><br>Ut wisi enim ad minim veniam, quis nostrud exerci tation commodo conse</div>
  <div class="tiny" style="left:184px;top:79px;width:41px">Lorem ipsum dolor sit amet, consectetuer adipiscing elit, sed diam nonummy nibh euismod tincidunt ut laoreet dolore magna aliquam erat volutpat.<br><br>Ut wisi enim ad minim veniam, quis nostrud exerci tation commodo conse</div>
  <div class="footer"><span class="brand-dot"></span>©2023. Verran Hale Consulting Ltd</div>
  <div class="page-no">3</div>
</section>

<!-- 5 education -->
<section class="slide" style="left:320px;top:200px">
  <div class="slide-title">Our Education</div><div class="title-rule"></div>
  <div class="brand"><span class="brand-dot"></span>Verran Hale<br>Consulting</div>
  <svg style="left:0;top:0" width="267" height="151" viewBox="0 0 267 151">
    <g fill="none" stroke="#1f1f1f" stroke-width="1.6">
      <rect x="50" y="36" width="45" height="66" rx="4"/>
      <rect x="112" y="36" width="45" height="66" rx="4"/>
      <rect x="173" y="36" width="45" height="66" rx="4"/>
    </g>
    <g fill="#1f1f1f"><circle cx="94" cy="53" r="2"/><circle cx="112" cy="86" r="2"/><circle cx="157" cy="53" r="2"/><circle cx="173" cy="86" r="2"/></g>
    <g fill="none" stroke="var(--teal)" stroke-width=".8">
      <circle cx="72" cy="51" r="2.5"/><rect x="130" y="49" width="8" height="5"/><path d="M132 55 v-4 M135 55 v-6 M138 55 v-3"/>
    </g>
    <g font-family="Montserrat, sans-serif" font-size="3.6" font-weight="700" fill="var(--teal)" text-anchor="middle">
      <text x="72" y="63">IDEA</text><text x="134" y="63">PROMOTION</text><text x="195" y="63">GROWTH</text>
    </g>
  </svg>
  <div class="tiny" style="left:53px;top:67px;width:39px;text-align:center">Lorem ipsum dolor sit amet, consectetuer adipiscing elit, sed diam nonummy nibh euismod tincidunt ut laoreet dolore magna aliquam erat volutpat.</div>
  <div class="tiny" style="left:115px;top:67px;width:39px;text-align:center">Lorem ipsum dolor sit amet, consectetuer adipiscing elit, sed diam nonummy nibh euismod tincidunt ut laoreet dolore magna aliquam erat volutpat.</div>
  <div class="tiny" style="left:176px;top:67px;width:39px;text-align:center">Lorem ipsum dolor sit amet, consectetuer adipiscing elit, sed diam nonummy nibh euismod tincidunt ut laoreet dolore magna aliquam erat volutpat.</div>
  <div class="tiny" style="left:30px;top:112px;width:207px;text-align:center;font-size:2.8px">Lorem ipsum dolor sit amet, consectetuer adipiscing elit, sed diam nonummy nibh euismod tincidunt ut laoreet dolore magna aliquam erat volutpat. Ut wisi enim ad minim veniam, quis nostrud exerci tation ullamcorper suscipit lobortis nisl ut aliquip ex ea commodo consequat.</div>
  <div class="footer"><span class="brand-dot"></span>©2023. Verran Hale Consulting Ltd</div>
  <div class="page-no">4</div>
</section>

<!-- 6 list + dark panel -->
<section class="slide" style="left:601px;top:200px">
  <div class="slide-title">Text Added Hare</div><div class="title-rule"></div>
  <div class="brand"><span class="brand-dot"></span>Verran Hale<br>Consulting</div>
  <div style="left:30px;top:33px;width:95px">
    <div class="head teal" style="font-size:3.6px;font-weight:600">01. Aliquam Erat Volutpat</div><div class="tiny" style="padding-left:7px;margin-bottom:9px">Lorem ipsum dolor sit amet, consectetuer adipiscing elit, sed diam nonummy nibh euismod</div>
    <div class="head teal" style="font-size:3.6px;font-weight:600">02. Consectetuer Adipiscing Elit</div><div class="tiny" style="padding-left:7px;margin-bottom:9px">Lorem ipsum dolor sit amet, consectetuer adipiscing elit, sed diam nonummy nibh euismod tincidunt ut laoreet</div>
    <div class="head teal" style="font-size:3.6px;font-weight:600">03. Duis Autem Vel Eum</div><div class="tiny" style="padding-left:7px;margin-bottom:9px">Lorem ipsum dolor sit amet, consectetuer adipiscing elit, sed diam nonummy nibh euismod tincidunt.</div>
    <div class="head teal" style="font-size:3.6px;font-weight:600">04. Aliquam Erat Volutpat</div><div class="tiny" style="padding-left:7px">Lorem ipsum dolor sit amet, consectetuer adipiscing elit, sed diam nonummy nibh euismod tincidunt ut laoreet.</div>
  </div>
  <div style="left:147px;top:31px;width:92px;height:94px;background:#1f1f1f"></div>
  <div class="icon-circle" style="left:138px;top:40px;width:20px;height:20px;border:2px solid #fff"></div>
  <div class="icon-circle" style="left:138px;top:67px;width:20px;height:20px;border:2px solid #fff"></div>
  <div class="icon-circle" style="left:138px;top:96px;width:20px;height:20px;border:2px solid #fff"></div>
  <div style="left:163px;top:40px;width:72px"><div style="font-size:5px;font-weight:600;color:var(--teal)">Lorem ipsum</div><div class="tiny" style="color:#ddd">ipsum dolor sit amet, cons ectetuer adipiscing elit, sed diam nonummy nibh euismod tincidunt ut laoreet</div></div>
  <div style="left:163px;top:67px;width:72px"><div style="font-size:5px;font-weight:600;color:var(--teal)">Lorem ipsum</div><div class="tiny" style="color:#ddd">ipsum dolor sit amet, cons ectetuer adipiscing elit, sed diam nonummy nibh euismod tincidunt ut laoreet</div></div>
  <div style="left:163px;top:96px;width:72px"><div style="font-size:5px;font-weight:600;color:var(--teal)">Lorem ipsum</div><div class="tiny" style="color:#ddd">ipsum dolor sit amet, cons ectetuer adipiscing elit, sed diam nonummy nibh euismod tincidunt</div></div>
  <div class="footer"><span class="brand-dot"></span>©2023. Verran Hale Consulting Ltd</div>
  <div class="page-no">5</div>
</section>

<!-- 7 six columns -->
<section class="slide" style="left:38px;top:362px">
  <div class="slide-title">Text Added Hare</div><div class="title-rule"></div>
  <div class="brand"><span class="brand-dot"></span>Verran Hale<br>Consulting</div>
  <div style="left:20px;top:36px;width:232px;display:grid;grid-template-columns:repeat(3,1fr);gap:10px 8px">
    <div><div class="head" style="font-size:3.6px;font-weight:600">1. Text Added Here</div><div class="tiny">Lorem ipsum dolor sit amet, cons ectetuer adipiscing elit, sed diam nonummy nibh euismod tincidunt ut laoreet dolore magna aliquam erat volutpat. Ut wisi enim ad minim veniam, quis nostrud exerci tation ullamcorper suscipit lobortis nisl ut aliquip.</div></div>
    <div><div class="head teal" style="font-size:3.6px;font-weight:600">1. Text Added Here</div><div class="tiny">Lorem ipsum dolor sit amet, cons ectetuer adipiscing elit, sed diam nonummy nibh euismod tincidunt ut laoreet dolore magna aliquam erat volutpat. Ut wisi enim ad minim veniam, quis nostrud exerci tation ullamcorper suscipit lobortis nisl ut aliquip.</div></div>
    <div><div class="head" style="font-size:3.6px;font-weight:600">1. Text Added Here</div><div class="tiny">Lorem ipsum dolor sit amet, cons ectetuer adipiscing elit, sed diam nonummy nibh euismod tincidunt ut laoreet dolore magna aliquam erat volutpat. Ut wisi enim ad minim veniam, quis nostrud exerci tation ullamcorper suscipit lobortis nisl ut aliquip.</div></div>
    <div><div class="head teal" style="font-size:3.6px;font-weight:600">1. Text Added Here</div><div class="tiny">Lorem ipsum dolor sit amet, cons ectetuer adipiscing elit, sed diam nonummy nibh euismod tincidunt ut laoreet dolore magna aliquam erat volutpat. Ut wisi enim ad minim veniam, quis nostrud exerci tation ullamcorper suscipit lobortis nisl ut aliquip.</div></div>
    <div><div class="head" style="font-size:3.6px;font-weight:600">1. Text Added Here</div><div class="tiny">Lorem ipsum dolor sit amet, cons ectetuer adipiscing elit, sed diam nonummy nibh euismod tincidunt ut laoreet dolore magna aliquam erat volutpat. Ut wisi enim ad minim veniam, quis nostrud exerci tation ullamcorper suscipit lobortis nisl ut aliquip.</div></div>
    <div><div class="head teal" style="font-size:3.6px;font-weight:600">1. Text Added Here</div><div class="tiny">Lorem ipsum dolor sit amet, cons ectetuer adipiscing elit, sed diam nonummy nibh euismod tincidunt ut laoreet dolore magna aliquam erat volutpat. Ut wisi enim ad minim veniam, quis nostrud exerci tation ullamcorper suscipit lobortis nisl ut aliquip.</div></div>
  </div>
  <div class="footer"><span class="brand-dot"></span>©2023. Verran Hale Consulting Ltd</div>
  <div class="page-no">6</div>
</section>

<!-- 8 section break -->
<section class="slide" style="left:320px;top:362px">
  <div role="img" aria-label="Teal-toned photograph of a stethoscope on a desk" style="left:12px;top:10px;width:243px;height:130px;background:linear-gradient(135deg,#1fb9ae,#28c4b9 55%,#159e95)"></div>
  <div style="left:40px;top:44px;width:50px;height:50px;border:2.5px solid rgba(255,255,255,.5);border-radius:50%"></div>
  <div style="left:109px;top:52px;color:#fff;font-size:13px;line-height:1.05;font-weight:400">Section<br><b style="font-weight:700">Break</b></div>
  <div style="left:109px;top:85px;width:115px;color:#fff;font-size:3.5px;line-height:1.3">Lorem ipsum dolor sit amet, consectetuer adipiscing elit sed diam nonummy nibh euismod tincid</div>
</section>

<!-- 9 values -->
<section class="slide" style="left:601px;top:362px">
  <div class="slide-title">Text Added Hare</div><div class="title-rule"></div>
  <div class="brand"><span class="brand-dot"></span>Verran Hale<br>Consulting</div>
  <div class="small" style="left:15px;top:34px;width:50px;font-size:3.6px">Lorem ipsum dolor sit amet,consectetuer adipiscing elit, sed diam nonummy nibh euismod tincidunt erat volutpat.<br><br>Ut wisi enim ad minim veniam, quis nostrud exerci tation ullamcorper suscipit lobortis nisl ut aliquip ex ea commodo consequat.</div>
  <div role="img" aria-label="Teal-tinted photograph of a businessman facing a digital health display" style="left:58px;top:20px;width:85px;height:119px;clip-path:polygon(55% 0,100% 0,45% 100%,0 100%);background:linear-gradient(160deg,#43d1c6,#137d77 55%,#2b2b2b)"></div>
  <div class="icon-circle" style="left:132px;top:32px;width:20px;height:20px;background:#fff;border:1.6px solid var(--teal)"></div>
  <div class="icon-circle" style="left:117px;top:67px;width:20px;height:20px;background:#fff;border:1.6px solid var(--teal)"></div>
  <div class="icon-circle" style="left:101px;top:102px;width:20px;height:20px;background:#fff;border:1.6px solid var(--teal)"></div>
  <div style="left:162px;top:36px;width:90px"><div class="head" style="font-size:4.6px">We Before Me</div><div class="tiny">ipsum dolor sit amet, cons ectetuer adipiscing elit, sed diam nonummy nibh euismod tincidunt ut laoreet</div></div>
  <div style="left:147px;top:71px;width:100px"><div class="head" style="font-size:4.6px">We Are Good People</div><div class="tiny">ipsum dolor sit amet, cons ectetuer adipiscing elit, sed diam nonummy nibh euismod tincidunt ut laoreet dolore magna aliquam erat volutpat.</div></div>
  <div style="left:130px;top:106px;width:100px"><div class="head" style="font-size:4.6px">We Work with Heart</div><div class="tiny">ipsum dolor sit amet, cons ectetuer adipiscing elit, sed diam nonummy nibh euismod tincidunt</div></div>
  <div class="footer"><span class="brand-dot"></span>©2023. Verran Hale Consulting Ltd</div>
  <div class="page-no">8</div>
</section>

<!-- 10 bar chart -->
<section class="slide" style="left:38px;top:525px">
  <div class="brand"><span class="brand-dot"></span>Verran Hale<br>Consulting</div>
  <div style="left:0;top:48px;width:92px;height:69px;background:var(--soft)"></div>
  <div style="left:12px;top:12px;font-size:8px;font-weight:700;line-height:1.3">Market<br>Opportunities.</div>
  <div class="title-rule" style="top:40px;left:12px;width:6px"></div>
  <div class="small" style="left:12px;top:56px;width:66px;font-size:3.7px">Lorem ipsum dolor sit amet, consectetuer adipiscing elit, sed diam nonummy nibh euismod tincidunt ut laoreet dolore magna aliquam erat volutpat. Ut wisi enim ad minim veniam, quis nostrud exerci tation ullamcorper suscipit lobortis nisl ut aliquip ex ea commodo consequat. Duis autem vel eum iriure dolor in hendrerit i</div>
  <div style="left:110px;top:18px;font-size:4px;font-weight:500;color:#444">CONSECTETUER ADIPISCING</div>
  <svg style="left:100px;top:28px" width="160" height="72" viewBox="0 0 160 72" font-family="Montserrat, sans-serif" font-size="4" fill="#333">
    <g stroke="#999" stroke-width=".4">
      <line x1="14" y1="2" x2="154" y2="2"/><line x1="14" y1="12.3" x2="154" y2="12.3"/><line x1="14" y1="22.7" x2="154" y2="22.7"/><line x1="14" y1="33" x2="154" y2="33"/><line x1="14" y1="43.3" x2="154" y2="43.3"/><line x1="14" y1="53.7" x2="154" y2="53.7"/><line x1="14" y1="64" x2="154" y2="64"/>
      <line x1="14" y1="2" x2="14" y2="64"/><line x1="154" y1="2" x2="154" y2="64"/>
    </g>
    <text x="2" y="3.5">60</text><text x="2" y="13.8">50</text><text x="2" y="24.2">40</text><text x="2" y="34.5">30</text><text x="2" y="44.8">20</text><text x="2" y="55.2">10</text><text x="5" y="65.5">0</text>
    <rect x="24" y="9.2" width="15" height="54.8" fill="#1f1f1f"/>
    <rect x="56" y="31" width="15" height="33" fill="var(--teal)"/>
    <rect x="88" y="15.4" width="15" height="48.6" fill="#1f1f1f"/>
    <rect x="120" y="36" width="15" height="28" fill="var(--teal)"/>
    <text x="27" y="71">JAN</text><text x="59" y="71">FEB</text><text x="91" y="71">MAR</text><text x="123" y="71">APR</text>
  </svg>
  <div style="left:108px;top:108px;width:66px"><div class="head" style="font-size:4.4px;font-weight:600"><span class="teal">●</span> Lorem ipsum</div><div class="tiny" style="padding-left:7px">Lorem ipsum dolor sit amet, consectetuer adipiscing elit, sed diam nonummy nibh euismod tincidunt ut laoreet</div></div>
  <div style="left:182px;top:108px;width:66px"><div class="head" style="font-size:4.4px;font-weight:600"><span class="teal">●</span> Lorem ipsum</div><div class="tiny" style="padding-left:7px">Lorem ipsum dolor sit amet, consectetuer adipiscing elit, sed diam nonummy nibh euismod tincidunt ut laoreet</div></div>
  <div class="footer"><span class="brand-dot"></span>©2023. Verran Hale Consulting Ltd</div>
  <div class="page-no">9</div>
</section>

<!-- 11 four cards -->
<section class="slide" style="left:320px;top:525px">
  <div class="slide-title">Text Added Hare</div><div class="title-rule"></div>
  <div class="brand"><span class="brand-dot"></span>Verran Hale<br>Consulting</div>
  <div style="left:39px;top:45px;width:188px;display:grid;grid-template-columns:repeat(4,1fr);gap:8px">
    <div style="position:relative;height:64px;border:.8px solid #1f1f1f;padding:10px 4px 0"><div class="icon-circle" style="position:absolute;left:15px;top:-7px;width:12px;height:12px"></div><div style="font-size:4px;font-weight:600;color:var(--teal)">Lorem ipsum</div><div class="tiny">ipsum dolor sit amet, cons ectetuer adipiscing elit, sed diam nonummy nibh euismod tincidunt<br><br>ipsum dolor sit amet, cons ectetuer adipiscing elit, sed diam nonummy</div></div>
    <div style="position:relative;height:64px;border:.8px solid #1f1f1f;padding:10px 4px 0"><div class="icon-circle" style="position:absolute;left:15px;top:-7px;width:12px;height:12px"></div><div style="font-size:4px;font-weight:600;color:var(--teal)">Lorem ipsum</div><div class="tiny">ipsum dolor sit amet, cons ectetuer adipiscing elit, sed diam nonummy nibh euismod tincidunt<br><br>ipsum dolor sit amet, cons ectetuer adipiscing elit, sed diam nonummy</div></div>
    <div style="position:relative;height:64px;border:.8px solid #1f1f1f;padding:10px 4px 0"><div class="icon-circle" style="position:absolute;left:15px;top:-7px;width:12px;height:12px"></div><div style="font-size:4px;font-weight:600;color:var(--teal)">Lorem ipsum</div><div class="tiny">ipsum dolor sit amet, cons ectetuer adipiscing elit, sed diam nonummy nibh euismod tincidunt<br><br>ipsum dolor sit amet, cons ectetuer adipiscing elit, sed diam nonummy</div></div>
    <div style="position:relative;height:64px;border:.8px solid #1f1f1f;padding:10px 4px 0"><div class="icon-circle" style="position:absolute;left:15px;top:-7px;width:12px;height:12px"></div><div style="font-size:4px;font-weight:600;color:var(--teal)">Lorem ipsum</div><div class="tiny">ipsum dolor sit amet, cons ectetuer adipiscing elit, sed diam nonummy nibh euismod tincidunt<br><br>ipsum dolor sit amet, cons ectetuer adipiscing elit, sed diam nonummy</div></div>
  </div>
  <div style="left:39px;top:115px;font-size:8px;font-weight:700">+ 35k</div>
  <div class="tiny" style="left:39px;top:127px;width:150px">Lorem ipsum dolor sit amet, consectetuer adipiscing elit, sed diam nonummy nibh euismod tincidunt ut laoreet dolore magna aliquam erat volutpat. Ut wisi enim ad minim veniam.</div>
  <div class="footer"><span class="brand-dot"></span>©2023. Verran Hale Consulting Ltd</div>
  <div class="page-no">10</div>
</section>

<!-- 12 cycle -->
<section class="slide" style="left:601px;top:525px">
  <div class="slide-title">Text Added Hare</div><div class="title-rule"></div>
  <div class="brand"><span class="brand-dot"></span>Verran Hale<br>Consulting</div>
  <div class="tiny" style="left:12px;top:31px;width:82px;font-size:2.8px">Lorem ipsum dolor sit amet, consectetuer adipiscing elit, sed diam nonummy nibh .<br><br>Ut wisi enim ad minim veniam, quis nostrud exerci tation ullamcorper suscipit lobortis. Ut wisi enim ad minim veniam, quis nostrud exerci tation ullamcorper suscipit lobortis. Ut wisi enim ad minim veniam, quis nostrud exerci tation ullamcorper suscipit lobortis.</div>
  <div style="left:18px;top:88px;width:70px"><div class="head" style="font-size:3.6px;font-weight:600"><span class="teal">●</span> Lorem Ipsum</div><div class="tiny" style="padding-left:5px">Lorem ipsum dolor sit amet, consectetuer adipiscing elit, sed diam nonummy nibh euismod tincidunt</div></div>
  <div style="left:18px;top:107px;width:70px"><div class="head" style="font-size:3.6px;font-weight:600"><span class="teal">●</span> Lorem Ipsum</div><div class="tiny" style="padding-left:5px">Lorem ipsum dolor sit amet, consectetuer adipiscing elit, sed diam nonummy nibh euismod tincidunt</div></div>
  <svg style="left:100px;top:22px" width="167" height="112" viewBox="0 0 167 112" font-family="Montserrat, sans-serif">
    <path d="M86 103 A46 46 0 1 0 47 40" fill="none" stroke="#1f1f1f" stroke-width="2.6"/>
    <path d="M44 40 l-4 -3 4 13 4 -13z" fill="#1f1f1f"/>
    <circle cx="120" cy="20" r="10" fill="var(--teal)" stroke="#fff" stroke-width="2"/><circle cx="120" cy="20" r="5" fill="#fff"/>
    <circle cx="128" cy="59" r="10" fill="var(--teal)" stroke="#fff" stroke-width="2"/><circle cx="128" cy="59" r="5" fill="#fff"/>
    <circle cx="100" cy="92" r="7" fill="var(--teal)" stroke="#fff" stroke-width="2"/>
    <circle cx="55" cy="75" r="5" fill="#fff" stroke="var(--teal)" stroke-width="1"/><circle cx="47" cy="62" r="1.5" fill="#1f1f1f"/>
    <g fill="#1f1f1f"><rect x="57" y="42" width="2" height="8"/><rect x="60" y="45" width="2" height="5"/><rect x="63" y="40" width="2" height="10"/></g>
    <text x="62" y="57" font-size="4" font-weight="700" text-anchor="middle" fill="#1f1f1f">MAIN TITLE</text>
    <text x="62" y="61" font-size="2" text-anchor="middle" fill="#666">Lorem ipsum dolor sit amet</text>
    <g font-size="3.2" font-weight="700" fill="#1f1f1f"><text x="142" y="20">Your Title</text><text x="145" y="63">Your Title</text><text x="142" y="100">Your Title</text><text x="19" y="82">Your Title</text></g>
    <g font-size="2.4" font-style="italic" fill="var(--teal)"><text x="133" y="6">85%</text><text x="108" y="51">80%</text><text x="78" y="75">50%</text><text x="112" y="104">75%</text></g>
  </svg>
  <div class="footer"><span class="brand-dot"></span>©2023. Verran Hale Consulting Ltd</div>
  <div class="page-no">11</div>
</section>

<!-- 13 options -->
<section class="slide" style="left:38px;top:688px">
  <div class="slide-title">Text Added Hare</div><div class="title-rule"></div>
  <div class="brand"><span class="brand-dot"></span>Verran Hale<br>Consulting</div>
  <svg style="left:18px;top:65px" width="30" height="30" viewBox="0 0 30 30"><path d="M0 0 h12 l15 15 -15 15 h-12 l15 -15z" fill="#e4e4e4"/></svg>
  <div role="img" aria-label="Photograph of chess pieces on wooden blocks" style="left:65px;top:32px;width:50px;height:59px;background:linear-gradient(180deg,#4a4a4a,#8d7b66)"></div>
  <div role="img" aria-label="Photograph of a scientist in a laboratory" style="left:130px;top:32px;width:50px;height:59px;background:linear-gradient(180deg,#e6ece8,#b7c6c0)"></div>
  <div role="img" aria-label="Photograph of a businessman celebrating" style="left:196px;top:32px;width:50px;height:59px;background:linear-gradient(180deg,#d4d4d4,#5b5b5b)"></div>
  <div style="left:65px;top:93px;width:50px"><div style="font-size:4.4px;font-weight:600">First <span class="teal">Option</span></div><div class="tiny">Lorem ipsum dolor sit consectetuer adipiscing elit, sed diam nonummy nibh euismod tincidunt ut dolore magna aliquam erat volutpat. Ut wisi enim ad minim veniam, quis nostrud</div></div>
  <div style="left:130px;top:93px;width:50px"><div style="font-size:4.4px;font-weight:600">Second <span class="teal">Option</span></div><div class="tiny">Lorem ipsum dolor sit consectetuer adipiscing elit, sed diam nonummy nibh euismod tincidunt ut dolore magna aliquam erat volutpat. Ut wisi enim ad minim veniam, quis nostrud</div></div>
  <div style="left:196px;top:93px;width:50px"><div style="font-size:4.4px;font-weight:600">Third <span class="teal">Option</span></div><div class="tiny">Lorem ipsum dolor sit consectetuer adipiscing elit, sed diam nonummy nibh euismod tincidunt ut dolore magna aliquam erat volutpat. Ut wisi enim ad minim veniam, quis nostrud</div></div>
  <div class="footer"><span class="brand-dot"></span>©2023. Verran Hale Consulting Ltd</div>
  <div class="page-no">12</div>
</section>

<!-- 14 projects -->
<section class="slide" style="left:320px;top:688px">
  <div class="slide-title">Text Added Hare</div><div class="title-rule"></div>
  <div class="brand"><span class="brand-dot"></span>Verran Hale<br>Consulting</div>
  <svg style="left:0;top:0" width="267" height="151" viewBox="0 0 267 151">
    <circle cx="61" cy="78" r="32" fill="#fff" stroke="#1f1f1f" stroke-width="2.4"/>
    <circle cx="61" cy="78" r="27" fill="var(--teal)"/>
    <circle cx="61" cy="78" r="13" fill="none" stroke="#fff" stroke-width="1.2"/>
    <g fill="none" stroke="#1f1f1f" stroke-width=".8"><path d="M95 66 L110 46 H132"/><path d="M100 78 H132"/><path d="M95 90 L110 110 H132"/></g>
    <g fill="#1f1f1f"><circle cx="142" cy="46" r="10"/><circle cx="142" cy="78" r="10"/><circle cx="142" cy="110" r="10"/></g>
    <g fill="none" stroke="#fff" stroke-width=".8"><circle cx="142" cy="46" r="4"/><circle cx="142" cy="78" r="4"/><circle cx="142" cy="110" r="4"/></g>
  </svg>
  <div style="left:161px;top:36px;width:90px"><div style="font-size:4.8px;font-weight:600;color:var(--teal)">Project name</div><div class="tiny" style="font-size:2.8px">Lorem ipsum dolor sit amet, nec an dictas equidem appellantur, ut has commune accommodare. Mea illum, ludus solet idpro.</div></div>
  <div style="left:161px;top:70px;width:90px"><div style="font-size:4.8px;font-weight:600;color:var(--teal)">Project name</div><div class="tiny" style="font-size:2.8px">Lorem ipsum dolor sit amet, nec an dictas equidem appellantur, ut has commune accommodare. Mea illum, ludus solet idpro.</div></div>
  <div style="left:161px;top:104px;width:90px"><div style="font-size:4.8px;font-weight:600;color:var(--teal)">Project name</div><div class="tiny" style="font-size:2.8px">Lorem ipsum dolor sit amet, nec an dictas equidem appellantur, ut has commune accommodare. Mea illum, ludus solet idpro.</div></div>
  <div class="footer"><span class="brand-dot"></span>©2023. Verran Hale Consulting Ltd</div>
  <div class="page-no">13</div>
</section>

<!-- 15 icon grid -->
<section class="slide" style="left:601px;top:688px">
  <div class="slide-title">Text Added Hare</div><div class="title-rule"></div>
  <div class="brand"><span class="brand-dot"></span>Verran Hale<br>Consulting</div>
  <div style="left:30px;top:31px;width:215px;display:grid;grid-template-columns:repeat(3,1fr);gap:8px 10px;text-align:center">
    <div><div style="width:19px;height:19px;margin:0 auto 3px;background:var(--teal)"></div><div style="font-size:4px;font-weight:600">Lorem ipsum</div><div class="tiny">Lorem ipsum dolor sit amet, consectetuer adipiscing elit, sed diam nonummy nibh euismod tincidunt ut laoreet</div></div>
    <div><div style="width:19px;height:19px;margin:0 auto 3px;background:#1f1f1f"></div><div style="font-size:4px;font-weight:600;color:var(--teal)">Lorem ipsum</div><div class="tiny">Lorem ipsum dolor sit amet, consectetuer adipiscing elit, sed diam nonummy nibh euismod tincidunt ut laoreet</div></div>
    <div><div style="width:19px;height:19px;margin:0 auto 3px;background:var(--teal)"></div><div style="font-size:4px;font-weight:600">Lorem ipsum</div><div class="tiny">Lorem ipsum dolor sit amet, consectetuer adipiscing elit, sed diam nonummy nibh euismod tincidunt ut laoreet</div></div>
    <div><div style="width:19px;height:19px;margin:0 auto 3px;background:#1f1f1f"></div><div style="font-size:4px;font-weight:600;color:var(--teal)">Lorem ipsum</div><div class="tiny">Lorem ipsum dolor sit amet, consectetuer adipiscing elit, sed diam nonummy nibh euismod tincidunt ut laoreet</div></div>
    <div><div style="width:19px;height:19px;margin:0 auto 3px;background:var(--teal)"></div><div style="font-size:4px;font-weight:600">Lorem ipsum</div><div class="tiny">Lorem ipsum dolor sit amet, consectetuer adipiscing elit, sed diam nonummy nibh euismod tincidunt ut laoreet</div></div>
    <div><div style="width:19px;height:19px;margin:0 auto 3px;background:#1f1f1f"></div><div style="font-size:4px;font-weight:600;color:var(--teal)">Lorem ipsum</div><div class="tiny">Lorem ipsum dolor sit amet, consectetuer adipiscing elit, sed diam nonummy nibh euismod tincidunt ut laoreet</div></div>
  </div>
  <div class="footer"><span class="brand-dot"></span>©2023. Verran Hale Consulting Ltd</div>
  <div class="page-no">14</div>
</section>

<!-- 16 timeline -->
<section class="slide" style="left:38px;top:850px">
  <div class="slide-title">Text Added Hare</div><div class="title-rule"></div>
  <div class="brand"><span class="brand-dot"></span>Verran Hale<br>Consulting</div>
  <svg style="left:0;top:0" width="267" height="151" viewBox="0 0 267 151" font-family="Montserrat, sans-serif">
    <line x1="31" y1="80" x2="236" y2="80" stroke="#888" stroke-width=".5"/>
    <g fill="none" stroke="var(--teal)" stroke-width="2.2">
      <path d="M40 80 V58 a6 6 0 0 1 6 -6 H76 a6 6 0 0 1 6 6 V80"/>
      <path d="M115 80 V58 a6 6 0 0 1 6 -6 H151 a6 6 0 0 1 6 6 V80"/>
      <path d="M190 80 V58 a6 6 0 0 1 6 -6 H226 a6 6 0 0 1 6 6 V80"/>
    </g>
    <g fill="none" stroke="#333" stroke-width="2.2">
      <path d="M78 80 V98 a6 6 0 0 0 6 6 H112 a6 6 0 0 0 6 -6 V80"/>
      <path d="M153 80 V98 a6 6 0 0 0 6 6 H187 a6 6 0 0 0 6 -6 V80"/>
    </g>
    <g fill="var(--teal)" stroke="#fff" stroke-width="1.5"><circle cx="61" cy="52" r="6"/><circle cx="136" cy="52" r="6"/><circle cx="211" cy="52" r="6"/></g>
    <g fill="#333" stroke="#fff" stroke-width="1.5"><circle cx="98" cy="104" r="6"/><circle cx="173" cy="104" r="6"/></g>
    <g font-size="8.5" font-weight="600" text-anchor="middle" fill="#1f1f1f"><text x="61" y="75">2018</text><text x="136" y="75">2020</text><text x="211" y="75">2022</text><text x="98" y="96">2019</text><text x="173" y="96">2021</text></g>
  </svg>
  <div style="left:82px;top:28px;width:34px;text-align:center"><div style="font-size:3px;font-weight:700">LOREM IPSUM</div><div class="tiny">Lorem ipsum dolor sit amet, consectetur adipiscing elit. Duis elit sapien, convallis vel enim sit amet, egestas commodo arcu.</div></div>
  <div style="left:157px;top:28px;width:34px;text-align:center"><div style="font-size:3px;font-weight:700">LOREM IPSUM</div><div class="tiny">Lorem ipsum dolor sit amet, consectetur adipiscing elit. Duis elit sapien, convallis vel enim sit amet, egestas commodo arcu.</div></div>
  <div style="left:44px;top:94px;width:34px;text-align:center"><div style="font-size:3px;font-weight:700">LOREM IPSUM</div><div class="tiny">Lorem ipsum dolor sit amet, consectetur adipiscing elit. Duis elit sapien, convallis vel enim sit amet, egestas commodo arcu.</div></div>
  <div style="left:119px;top:94px;width:34px;text-align:center"><div style="font-size:3px;font-weight:700">LOREM IPSUM</div><div class="tiny">Lorem ipsum dolor sit amet, consectetur adipiscing elit. Duis elit sapien, convallis vel enim sit amet, egestas commodo arcu.</div></div>
  <div style="left:194px;top:94px;width:34px;text-align:center"><div style="font-size:3px;font-weight:700">LOREM IPSUM</div><div class="tiny">Lorem ipsum dolor sit amet, consectetur adipiscing elit. Duis elit sapien, convallis vel enim sit amet, egestas commodo arcu.</div></div>
  <div class="footer"><span class="brand-dot"></span>©2023. Verran Hale Consulting Ltd</div>
  <div class="page-no">15</div>
</section>

<!-- 17 quadrant ring -->
<section class="slide" style="left:320px;top:850px">
  <div class="slide-title">Text Added Hare</div><div class="title-rule"></div>
  <div class="brand"><span class="brand-dot"></span>Verran Hale<br>Consulting</div>
  <svg style="left:0;top:0" width="267" height="151" viewBox="0 0 267 151" font-family="Montserrat, sans-serif">
    <path d="M134 78 L134 41 A37 37 0 0 0 97 78 Z" fill="#1f1f1f"/>
    <path d="M134 78 L171 78 A37 37 0 0 0 134 41 Z" fill="var(--teal)"/>
    <path d="M134 78 L134 115 A37 37 0 0 0 171 78 Z" fill="#1f1f1f"/>
    <path d="M134 78 L97 78 A37 37 0 0 0 134 115 Z" fill="var(--teal)"/>
    <g stroke="#fff" stroke-width="1.5"><line x1="134" y1="40" x2="134" y2="116"/><line x1="96" y1="78" x2="172" y2="78"/></g>
    <circle cx="134" cy="78" r="18" fill="#fff"/>
    <text x="134" y="77" font-size="6" font-weight="700" text-anchor="middle">Text</text>
    <text x="134" y="84" font-size="6" font-weight="700" text-anchor="middle">Added</text>
  </svg>
  <div style="left:28px;top:38px;width:64px;text-align:right"><div style="font-size:4.8px;font-weight:600;color:var(--teal)">Text Here</div><div class="tiny">Lorem ipsum dolor sit amet, consectetuer adipiscing elit, sed diammy nibh euismod tincidunt ut laoreet dolore</div></div>
  <div style="left:178px;top:38px;width:64px"><div style="font-size:4.8px;font-weight:600">Text Here</div><div class="tiny">Lorem ipsum dolor sit amet, consectetuer adipiscing elit, sed diammy nibh euismod tincidunt ut laoreet dolore</div></div>
  <div style="left:28px;top:96px;width:64px;text-align:right"><div style="font-size:4.8px;font-weight:600">Text Here</div><div class="tiny">Lorem ipsum dolor sit amet, consectetuer adipiscing elit, sed diammy nibh euismod tincidunt ut laoreet dolore</div></div>
  <div style="left:178px;top:96px;width:64px"><div style="font-size:4.8px;font-weight:600;color:var(--teal)">Text Here</div><div class="tiny">Lorem ipsum dolor sit amet, consectetuer adipiscing elit, sed diammy nibh euismod tincidunt ut laoreet dolore</div></div>
  <div class="footer"><span class="brand-dot"></span>©2023. Verran Hale Consulting Ltd</div>
  <div class="page-no">16</div>
</section>

<!-- 18 steps -->
<section class="slide" style="left:601px;top:850px">
  <div class="slide-title">Text Added Hare</div><div class="title-rule"></div>
  <div class="brand"><span class="brand-dot"></span>Verran Hale<br>Consulting</div>
  <svg style="left:25px;top:47px" width="220" height="26" viewBox="0 0 220 26" font-family="Montserrat, sans-serif" font-size="4.6" font-weight="600" fill="#fff" text-anchor="middle">
    <polygon points="0,0 38,0 47,13 38,26 0,26 9,13" fill="var(--teal)"/>
    <polygon points="42,0 80,0 89,13 80,26 42,26 51,13" fill="#1f1f1f"/>
    <polygon points="84,0 122,0 131,13 122,26 84,26 93,13" fill="var(--teal)"/>
    <polygon points="126,0 164,0 173,13 164,26 126,26 135,13" fill="#1f1f1f"/>
    <polygon points="168,0 206,0 215,13 206,26 168,26 177,13" fill="var(--teal)"/>
    <text x="26" y="15">STEP 01</text><text x="68" y="15">STEP 02</text><text x="110" y="15">STEP 03</text><text x="152" y="15">STEP 04</text><text x="194" y="15">STEP 05</text>
  </svg>
  <div style="left:25px;top:82px;width:215px;display:grid;grid-template-columns:repeat(5,1fr);gap:4px;text-align:center">
    <div><div style="font-size:4px;font-weight:600">Project name</div><div class="tiny">Lorem Ipsum is simply dummy unknown printer took a galley of type and scrambled it to make.</div></div>
    <div><div style="font-size:4px;font-weight:600;color:var(--teal)">Project name</div><div class="tiny">Lorem Ipsum is simply dummy unknown printer took a galley of type and scrambled it to make.</div></div>
    <div><div style="font-size:4px;font-weight:600">Project name</div><div class="tiny">Lorem Ipsum is simply dummy unknown printer took a galley of type and scrambled it to make.</div></div>
    <div><div style="font-size:4px;font-weight:600;color:var(--teal)">Project name</div><div class="tiny">Lorem Ipsum is simply dummy unknown printer took a galley of type and scrambled it to make.</div></div>
    <div><div style="font-size:4px;font-weight:600">Project name</div><div class="tiny">Lorem Ipsum is simply dummy unknown printer took a galley of type and scrambled it to make.</div></div>
  </div>
  <div class="footer"><span class="brand-dot"></span>©2023. Verran Hale Consulting Ltd</div>
  <div class="page-no">17</div>
</section>

<!-- 19 phones -->
<section class="slide" style="left:38px;top:1014px">
  <div class="slide-title">Text Added Hare</div><div class="title-rule"></div>
  <div class="brand"><span class="brand-dot"></span>Verran Hale<br>Consulting</div>
  <div style="left:118px;top:45px;width:95px;height:95px;border:6px solid #f2f2f2;border-radius:50%"></div>
  <div class="tiny" style="left:11px;top:30px;width:85px;font-size:2.8px">Lorem ipsum dolor sit amet, consectetuer adipiscing elit, sed diam nonummy nibh euismod tincidunt ut laoreet dolore magna aliquam erat volutpat. Ut wisi enim ad minim veniam,<br><br>quis nostrud exerci tation ullamcorper suscipit lobortis nisl ut aliquip ex ea commodo consequat. Duis autem vel eum iriure dolor in hendrerit in vulputate velit esse</div>
  <div style="left:19px;top:78px;width:80px">
    <div style="display:flex;gap:3px;margin-bottom:7px"><span style="flex:none;width:7px;height:7px;background:var(--teal);color:#fff;font-size:4.5px;font-weight:700;text-align:center;line-height:7px">1.</span><div><div style="font-size:3.6px;font-weight:600">Lorem ipsum</div><div class="tiny">Lorem ipsum dolor sit amet, consectetuer adipiscing elit, sed diam nonummy nibh euismod tincid</div></div></div>
    <div style="display:flex;gap:3px;margin-bottom:7px"><span style="flex:none;width:7px;height:7px;background:var(--teal);color:#fff;font-size:4.5px;font-weight:700;text-align:center;line-height:7px">2.</span><div><div style="font-size:3.6px;font-weight:600">Lorem ipsum</div><div class="tiny">Lorem ipsum dolor sit amet, consectetuer adipiscing elit, sed diam nonummy nibh euismod tincid</div></div></div>
    <div style="display:flex;gap:3px"><span style="flex:none;width:7px;height:7px;background:var(--teal);color:#fff;font-size:4.5px;font-weight:700;text-align:center;line-height:7px">3.</span><div><div style="font-size:3.6px;font-weight:600">Lorem ipsum</div><div class="tiny">Lorem ipsum dolor sit amet, consectetuer adipiscing elit, sed diam nonummy nibh euismod tincid</div></div></div>
  </div>
  <div style="left:119px;top:20px;width:32px;height:66px;border:1.4px solid #333;border-radius:4px;background:#fff;padding:7px 3px"><div style="font-size:3.6px;font-weight:500;line-height:1.2">Lorem ipsum dolor</div><div style="width:8px;height:6px;border:.6px solid var(--teal);margin:4px auto"></div><div class="tiny" style="font-size:1.8px;text-align:center">To introduce the students to the changing landscape of marketing and equip them with knowledge</div></div>
  <div style="left:159px;top:42px;width:32px;height:66px;border:1.4px solid #333;border-radius:4px;background:#fff;padding:7px 3px"><div style="font-size:3.6px;font-weight:500;line-height:1.2">Dolor sit amet, conse</div><div style="width:8px;height:8px;border:.6px solid var(--teal);border-radius:50%;margin:4px auto"></div><div class="tiny" style="font-size:1.8px;text-align:center">You will learn concepts and ideas in digital marketing as well as how to use different tools</div></div>
  <div style="left:199px;top:64px;width:32px;height:66px;border:1.4px solid #333;border-radius:4px;background:#fff;padding:7px 3px"><div style="font-size:3.6px;font-weight:500;line-height:1.2">Consec</div><div style="width:8px;height:8px;border:.6px solid var(--teal);border-radius:50%;margin:6px auto"></div><div class="tiny" style="font-size:1.8px;text-align:center">You are required to pass 80% of the evaluation test to obtain the certificate</div></div>
  <div class="footer"><span class="brand-dot"></span>©2023. Verran Hale Consulting Ltd</div>
  <div class="page-no">17</div>
</section>

<!-- 20 team -->
<section class="slide" style="left:320px;top:1014px">
  <div class="slide-title">Text Added Hare</div><div class="title-rule"></div>
  <div class="brand"><span class="brand-dot"></span>Verran Hale<br>Consulting</div>
  <div style="left:24px;top:43px;width:220px;display:grid;grid-template-columns:repeat(4,1fr);gap:21px;text-align:center">
    <div style="position:relative;padding-top:20px"><div style="position:absolute;left:0;top:0;width:100%;height:16px;background:#1f1f1f"></div><div role="img" aria-label="Team member portrait" style="position:absolute;left:50%;top:4px;width:20px;height:20px;margin-left:-10px;border-radius:50%;background:#c9c9c9;border:1.5px solid #fff"></div><div style="margin-top:10px;font-size:4.4px;font-weight:700;color:var(--teal)">JOHN SMITH</div><div class="tiny">ipsum dolor sit amet, cons ectetuer adipiscing elit, sed diam nonummy nibh euismod tincidunt</div></div>
    <div style="position:relative;padding-top:20px"><div style="position:absolute;left:0;top:0;width:100%;height:16px;background:var(--teal)"></div><div role="img" aria-label="Team member portrait" style="position:absolute;left:50%;top:4px;width:20px;height:20px;margin-left:-10px;border-radius:50%;background:#c9c9c9;border:1.5px solid #fff"></div><div style="margin-top:10px;font-size:4.4px;font-weight:700">MILLIE SMITH</div><div class="tiny">ipsum dolor sit amet, cons ectetuer adipiscing elit, sed diam nonummy nibh euismod tincidunt</div></div>
    <div style="position:relative;padding-top:20px"><div style="position:absolute;left:0;top:0;width:100%;height:16px;background:#1f1f1f"></div><div role="img" aria-label="Team member portrait" style="position:absolute;left:50%;top:4px;width:20px;height:20px;margin-left:-10px;border-radius:50%;background:#c9c9c9;border:1.5px solid #fff"></div><div style="margin-top:10px;font-size:4.4px;font-weight:700;color:var(--teal)">JOHN SMITH</div><div class="tiny">ipsum dolor sit amet, cons ectetuer adipiscing elit, sed diam nonummy nibh euismod tincidunt</div></div>
    <div style="position:relative;padding-top:20px"><div style="position:absolute;left:0;top:0;width:100%;height:16px;background:var(--teal)"></div><div role="img" aria-label="Team member portrait" style="position:absolute;left:50%;top:4px;width:20px;height:20px;margin-left:-10px;border-radius:50%;background:#c9c9c9;border:1.5px solid #fff"></div><div style="margin-top:10px;font-size:4.4px;font-weight:700">MILLIE SMITH</div><div class="tiny">ipsum dolor sit amet, cons ectetuer adipiscing elit, sed diam nonummy nibh euismod tincidunt</div></div>
  </div>
  <div class="footer"><span class="brand-dot"></span>©2023. Verran Hale Consulting Ltd</div>
  <div class="page-no">18</div>
</section>

<!-- 21 thank you -->
<section class="slide" style="left:601px;top:1014px">
  <div style="left:-20px;top:15px;width:125px;height:125px;border:6px solid #f2f2f2;border-radius:50%"></div>
  <div style="left:141px;top:34px;font-size:9.5px;font-weight:500;line-height:1.05">Verran Hale<br><span style="font-weight:400">Consulting</span></div>
  <div style="left:141px;top:63px;font-size:15px;font-weight:800">Thank You</div>
  <svg style="left:142px;top:87px" width="10" height="48" viewBox="0 0 10 48" fill="var(--teal)">
    <path d="M1 1 l2 -1 2 3 -1 1 q1 2 3 3 l1 -1 3 2 -1 2 q-6 0 -9 -9z"/>
    <path d="M0 20 l9 -3 -3 9 -1.5 -4z"/>
    <path d="M4.5 32 l-4.5 4 h1.5 v4 h6 v-4 h1.5z"/>
  </svg>
  <div style="left:152px;top:87px;width:.5px;height:7px;background:#333"></div>
  <div style="left:152px;top:102px;width:.5px;height:7px;background:#333"></div>
  <div style="left:152px;top:118px;width:.5px;height:7px;background:#333"></div>
  <div style="left:156px;top:87px;font-size:3.6px;line-height:1.3;color:#444">+18 2767 9470 1808<br>+18 2767 9470 1808</div>
  <div style="left:156px;top:102px;font-size:3.6px;line-height:1.3;color:#444">www.websitename.com<br>urname@email.com</div>
  <div style="left:156px;top:118px;font-size:3.6px;line-height:1.3;color:#444">1234 Street name, town/city,<br>state/country, post/zip 012345.</div>
  <div style="left:92px;top:145px;width:175px;height:6px;background:var(--teal);clip-path:polygon(4% 0,100% 0,100% 100%,0 100%)"></div>
</section>

</main>
</body>
</html>
```